依頼詳細
●商品概要
本商品は、A4用紙250ページの書籍です。

●デザインに入れていただきたいポイント、キーワード
・「共通の道具、認識、言語が1つになった魔法の書」
・「仕組み化の解体新書」
・「総ページ数250P以上の圧倒的ボリューム」
・「社内教育テキストの決定版」
記載項目
商品名「風見鶏の航海日誌録」
商品画像は添付ファイルをご確認、デザインにご利用ください
サイズ
• 縦370px, 横850px
希望イメージ
シンプル 複雑
単色 カラフル
暗い 明るい
日常 高級
遊び心 厳粛
未来的 伝統的
女性的 男性的
希望する色
青系、緑系、黄・オレンジ系
納品ファイル
• イラストレーター形式 (.ai)
• フォトショップ形式 (.psd)
補足説明
納品ファイルは指定のいずれかでお願いします。
納品していただいたファイルはこちらで一部修正して利用する場合がありますので予めご了承ください。
画像のファイルを添付致しました。

小さい画面で見た時にも文字が見やすく伝わりやすいと感じました。

この度は弊社の依頼にたくさんのご提案を頂きまして誠にありがとうございました。正直、どのご提案も素晴らしく、非常に選定に迷いました。また機会がございましたらよろしくお願い申し上げます。

```html
<!DOCTYPE html>
<html lang="ja">
<head>
<meta charset="utf-8">
<title>風見鶏の航海日誌録 バナー案</title>
<link href="https://fonts.googleapis.com/css2?family=Noto+Serif+JP:wght@700;900&family=Noto+Sans+JP:wght@700;900&display=swap" rel="stylesheet">
<style>
  :root{
    --canvas:#ffffff;
    --ink:#111111;
    --accent-red:#e0141b;
    --title-blue:#1a3aa6;
    --title-yellow:#ffe600;
    --outline-violet:#1a0f5a;
    --shadow-navy:#06104a;
    --gold-a:#ffd43a;
    --gold-b:#ff9e12;
    --violet-a:#6f7cf0;
    --violet-b:#2a1f9a;
    --navy-a:#3b5fe0;
    --navy-b:#0d1f86;
    --button-a:#ff4a2a;
    --button-b:#c8060c;
    --button-edge:#7a0206;
    --frame:#d9d9d9;
  }
  html,body{margin:0;padding:0;overflow:hidden;}
  body{width:818px;height:1200px;background:var(--canvas);}
  .sheet{position:relative;width:818px;height:1200px;padding:20px 0;box-sizing:border-box;display:flex;flex-direction:column;gap:25px;}
  .banner{position:relative;width:818px;height:370px;overflow:hidden;border:1px solid var(--frame);box-sizing:border-box;}
  .points{position:absolute;left:0;top:0;width:410px;height:100%;padding:26px 0 0 18px;box-sizing:border-box;
    font-family:"Noto Serif JP",serif;font-weight:900;color:var(--ink);}
  .point{display:flex;align-items:flex-start;gap:10px;font-size:27px;line-height:1.3;margin-bottom:22px;white-space:nowrap;}
  .point .tick{flex:0 0 30px;width:30px;height:30px;margin-top:4px;}
  .point .hl{color:var(--accent-red);}
  .point .ul{border-bottom:3px solid var(--accent-red);}
  .brand{position:absolute;top:12px;right:22px;font-family:"Noto Sans JP",sans-serif;font-weight:700;font-size:18px;color:var(--ink);}
  .title{position:absolute;left:420px;top:60px;width:380px;margin:0;text-align:center;font-family:"Noto Sans JP",sans-serif;font-weight:900;line-height:1.05;}
  .title .l1{display:block;font-size:84px;letter-spacing:2px;}
  .title .l2{display:block;font-size:66px;margin-top:6px;}
  .cta{position:absolute;left:432px;bottom:34px;width:358px;height:72px;border-radius:10px;
    background:linear-gradient(var(--button-a),var(--button-b));color:#fff;font-family:"Noto Sans JP",sans-serif;
    font-weight:900;font-size:38px;display:flex;align-items:center;justify-content:center;box-shadow:0 3px 0 var(--button-edge);}
  .banner--warm{background:linear-gradient(90deg,var(--gold-a) 0,var(--gold-b) 45%,#fff 55%,#f1f1f1 100%);}
  .banner--warm .title{color:var(--title-blue);}
  .banner--violet{background:linear-gradient(90deg,#fff 0,#fff 48%,var(--violet-a) 55%,var(--violet-b) 100%);}
  .banner--violet .title{color:var(--title-yellow);
    text-shadow:2px 0 0 var(--outline-violet),-2px 0 0 var(--outline-violet),0 2px 0 var(--outline-violet),0 -2px 0 var(--outline-violet),
      2px 2px 0 var(--outline-violet),-2px 2px 0 var(--outline-violet),2px -2px 0 var(--outline-violet),-2px -2px 0 var(--outline-violet);}
  .banner--violet .brand{color:#fff;}
  .banner--navy{background:linear-gradient(90deg,#fff 0,#fff 48%,var(--navy-a) 55%,var(--navy-b) 100%);}
  .banner--navy .title{color:var(--title-yellow);text-shadow:3px 3px 0 var(--shadow-navy);}
  .banner--navy .brand{color:#fff;}
</style>
</head>
<body>
<svg width="0" height="0" style="position:absolute">
  <symbol id="tick" viewBox="0 0 32 32">
    <rect x="2" y="6" width="22" height="22" fill="#fff" stroke="#444" stroke-width="2"/>
    <path d="M6 16 L12 24 L29 3" fill="none" stroke="#d8101a" stroke-width="5" stroke-linecap="round" stroke-linejoin="round"/>
  </symbol>
</svg>
<main class="sheet">
  <section class="banner banner--warm">
    <div class="points">
      <div class="point"><svg class="tick"><use href="#tick"/></svg><span>共通の道具、認識、言語が<br><span class="ul">1つになった<span class="hl">魔法の書</span></span></span></div>
      <div class="point"><svg class="tick"><use href="#tick"/></svg><span class="ul">仕組み化の<span class="hl">解体新書</span></span></div>
      <div class="point"><svg class="tick"><use href="#tick"/></svg><span>総ページ数250P以上の<br>圧倒的ボリューム</span></div>
      <div class="point"><svg class="tick"><use href="#tick"/></svg><span>社内教育テキストの決定版</span></div>
    </div>
    <div class="brand">Corvella</div>
    <h2 class="title"><span class="l1">風見鶏の</span><span class="l2">航海日誌録</span></h2>
    <div class="cta">詳細はこちら≫</div>
  </section>
  <section class="banner banner--violet">
    <div class="points">
      <div class="point"><svg class="tick"><use href="#tick"/></svg><span>共通の道具、認識、言語が<br>1つになった魔法の書</span></div>
      <div class="point"><svg class="tick"><use href="#tick"/></svg><span>仕組み化の解体新書</span></div>
      <div class="point"><svg class="tick"><use href="#tick"/></svg><span>総ページ数250P以上の<br>圧倒的ボリューム</span></div>
      <div class="point"><svg class="tick"><use href="#tick"/></svg><span>社内教育テキストの決定版</span></div>
    </div>
    <div class="brand">Corvella</div>
    <h2 class="title"><span class="l1">風見鶏の</span><span class="l2">航海日誌録</span></h2>
    <div class="cta">詳細はこちら≫</div>
  </section>
  <section class="banner banner--navy">
    <div class="points">
      <div class="point"><svg class="tick"><use href="#tick"/></svg><span>共通の道具、認識、言語が<br>1つになった魔法の書</span></div>
      <div class="point"><svg class="tick"><use href="#tick"/></svg><span>仕組み化の解体新書</span></div>
      <div class="point"><svg class="tick"><use href="#tick"/></svg><span>総ページ数250P以上の<br>圧倒的ボリューム</span></div>
      <div class="point"><svg class="tick"><use href="#tick"/></svg><span>社内教育テキストの決定版</span></div>
    </div>
    <div class="brand">Corvella</div>
    <h2 class="title"><span class="l1">風見鶏の</span><span class="l2">航海日誌録</span></h2>
    <div class="cta">詳細はこちら≫</div>
  </section>
</main>
</body>
</html>
```